Brenwick Holdings Limited
BrenHold
I agree with jonwel. The logo's resolution is too low. Please provide an Adobe Illustrator File or a larger logo. Thanks.
#7 obviously doesn't get the fact that this is a business card, not a logo. :-)
H! GT please provide eps or ai files for the logo, the png file is too small and not a transparent.. Thanks!

```html
<!DOCTYPE html>
<html lang="en">
<head>
<meta charset="utf-8">
<title>BrenHold business card</title>
<link rel="stylesheet" href="https://fonts.googleapis.com/css2?family=PT+Sans+Narrow:wght@400;700&display=swap">
<style>
  :root {
    --backdrop: #ababab;
    --card: #ffffff;
    --navy: #1f3f7a;
    --blue: #2b7fc4;
    --phone-bar: #f0643c;
    --phone-fill: #fbc3b2;
    --phone-ink: #ee5a30;
    --cell-bar: #2b8ad0;
    --cell-fill: #a8cbe9;
    --cell-ink: #2178c0;
    --fax-bar: #1f3f7a;
    --fax-fill: #a7b7cf;
    --fax-ink: #1f3f7a;
    --mail-bar: #8cbf2a;
    --mail-fill: #dce8a9;
    --mail-ink: #7aaa20;
  }
  * { box-sizing: border-box; margin: 0; padding: 0; }
  html, body { width: 1200px; height: 929px; overflow: hidden; }
  body {
    background: var(--backdrop);
    font-family: "PT Sans Narrow", sans-serif;
    position: relative;
  }
  .card {
    position: absolute;
    left: 261px; top: 256px;
    width: 668px; height: 382px;
    background: var(--card);
    overflow: hidden;
  }
  .identity {
    position: absolute; left: 10px; top: 16px;
    font-size: 19px; color: var(--navy);
  }
  .identity .role { color: var(--blue); }
  .identity .divider { color: var(--navy); margin: 0 3px; }
  .address {
    position: absolute; right: 174px; top: 10px;
    text-align: right; font-size: 15px; line-height: 16.5px;
    font-style: normal; font-weight: 400;
    color: var(--navy);
  }
  .brand {
    position: absolute; left: 512px; top: 26px;
    display: flex; align-items: center; gap: 8px;
    font-size: 26px; color: var(--navy);
  }
  .brand .mark { width: 14px; height: 14px; background: var(--blue); }
  .contacts {
    position: absolute; left: 0; top: 106px;
    width: 668px; height: 276px;
  }
  .contact {
    position: absolute; top: 0; height: 276px;
  }
  .contact .tab {
    height: 14px; position: relative;
  }
  .contact .tab::after {
    content: ""; position: absolute; left: 0; right: 0; bottom: 0;
    height: 5px; background: var(--bar);
  }
  .contact .label {
    position: absolute; left: 0; top: 0;
    background: var(--bar); color: #fff;
    font-size: 10px; line-height: 10px; padding: 0 12px 0 4px;
  }
  .contact .body {
    height: 262px; background: var(--fill);
    padding: 6px 0 0 5px;
  }
  .contact .value {
    font-size: 23px; color: var(--ink); white-space: nowrap;
  }
  .contact.mail .value { font-size: 14px; letter-spacing: -0.1px; padding-top: 6px; }
  .phone { left: 0; width: 161px; --bar: var(--phone-bar); --fill: var(--phone-fill); --ink: var(--phone-ink); }
  .cell { left: 171px; width: 156px; --bar: var(--cell-bar); --fill: var(--cell-fill); --ink: var(--cell-ink); }
  .fax { left: 337px; width: 158px; --bar: var(--fax-bar); --fill: var(--fax-fill); --ink: var(--fax-ink); }
  .mail { left: 507px; width: 161px; --bar: var(--mail-bar); --fill: var(--mail-fill); --ink: var(--mail-ink); }
</style>
</head>
<body>
  <main class="card">
    <p class="identity">Thomas R Vale<span class="divider">|</span><span class="role">Chief Executive</span></p>
    <address class="address">
      Harbour House<br>Kestrel Way<br>Elmbridge<br>Westshire<br>WE4 7QN
    </address>
    <div class="brand"><span class="mark"></span><span class="name">BrenHold</span></div>
    <section class="contacts">
      <div class="contact phone">
        <div class="tab"><span class="label">phone</span></div>
        <div class="body"><p class="value">+44 200 555 0181</p></div>
      </div>
      <div class="contact cell">
        <div class="tab"><span class="label">cell</span></div>
        <div class="body"><p class="value">+44 700 555 0142</p></div>
      </div>
      <div class="contact fax">
        <div class="tab"><span class="label">fax</span></div>
        <div class="body"><p class="value">+44 200 555 0199</p></div>
      </div>
      <div class="contact mail">
        <div class="tab"><span class="label">email</span></div>
        <div class="body"><p class="value">tom.vale@brenhold.example</p></div>
      </div>
    </section>
  </main>
</body>
</html>
```